New Alcoholic Spiked Seltzer Line

We need a can design for a line of low calorie alcoholic seltzer. This product is a sparkling water and vodka drink with no sugar added in a slim 12 oz can.

This is a lighter, healthier, alternative to the sugary ready-to-drinks on the market. The product contains only 3 ingredients: Vodka, Water and Natural Flavors. It has only 100 calories but still has 5% alcohol, so you don't need to sacrifice alcohol to cut calories.

This product also does not contain any preservatives.

We want this design to communicate the following objectives to the consumer and in this order:

1. Appetizing product
2.Low calorie
3.Communicate the type of beverage (Spiked Seltzer)

The brand name of the product is VELKA.

The flavor of the product needed to be used for the design is Mango-Orange.

Comparable products are:

www.brisavelfizz.example/
https://www.tarnowbubble.example
https://quellrind.example/

The designs should not infringe or copy the creative directions of the products mentionned above. They are only given so that you can better understand the type of product we are developing.

Target Market(s)

Young Professional women between the ages of 25 and 44

Industry/Entity Type

Product

Colors

Designer to choose colors to be used in the design.

Requirements
Must have
• Design extendibility, meaning it can be adapted for other flavors.
• This is a new category in the market we are targeting, so consumers must easily be able to identify what type of product this is.

```html
<!DOCTYPE html>
<html lang="en">
<head>
<meta charset="utf-8">
<title>VELKA Mango-Orange Vodka Spiked Seltzer – Can Label</title>
<link rel="stylesheet" href="https://fonts.googleapis.com/css2?family=Montserrat:wght@400;600&family=Oswald:wght@300&display=swap">
<style>
  :root {
    --backdrop: #e4e5e7;
    --label-white: #fbfbfa;
    --sun-yellow: #f7b81a;
    --ray-glow: #fbe6a4;
    --cream-band: #fbeed2;
    --peach-band: #f9d9a8;
    --mango-yellow: #fac21a;
    --brand-plum: #6a1c4d;
    --ink: #2a2420;
  }
  * { margin: 0; padding: 0; box-sizing: border-box; }
  html, body {
    width: 1200px;
    height: 800px;
    overflow: hidden;
    background: var(--backdrop);
  }
  .canvas {
    position: relative;
    width: 1200px;
    height: 800px;
    display: flex;
    align-items: center;
    justify-content: center;
  }
  .can-label {
    position: relative;
    width: 360px;
    height: 680px;
    background: var(--label-white);
    overflow: hidden;
    box-shadow: 0 10px 30px rgba(0,0,0,0.08);
  }
  .label-art {
    position: absolute;
    inset: 0;
    width: 100%;
    height: 100%;
  }
  .calorie-count {
    position: absolute;
    top: 60px;
    width: 100%;
    text-align: center;
    font-family: "Montserrat", sans-serif;
    font-weight: 400;
    font-size: 13px;
    letter-spacing: 2px;
    color: var(--ink);
  }
  .brand-name {
    position: absolute;
    top: 272px;
    width: 100%;
    text-align: center;
    font-family: "Montserrat", sans-serif;
    font-weight: 600;
    font-size: 44px;
    letter-spacing: 3px;
    color: var(--brand-plum);
  }
  .flavor-name {
    position: absolute;
    top: 522px;
    width: 100%;
    text-align: center;
    font-family: "Oswald", sans-serif;
    font-weight: 300;
    font-size: 46px;
    line-height: 1;
    color: var(--ink);
  }
  .beverage-type {
    position: absolute;
    top: 584px;
    width: 100%;
    text-align: center;
    font-family: "Montserrat", sans-serif;
    font-weight: 600;
    font-size: 13px;
    letter-spacing: 3px;
    color: var(--ink);
  }
  .product-facts {
    position: absolute;
    top: 630px;
    width: 100%;
    display: flex;
    justify-content: center;
    gap: 22px;
    font-family: "Montserrat", sans-serif;
    font-weight: 400;
    font-size: 13px;
    letter-spacing: 2px;
    color: var(--ink);
  }
</style>
</head>
<body>
  <main class="canvas">
    <section class="can-label">
      <svg class="label-art" viewBox="0 0 360 680" aria-hidden="true">
        <defs>
          <radialGradient id="sunburstGlow" cx="50%" cy="50%" r="50%">
            <stop offset="0%" stop-color="var(--ray-glow)" stop-opacity="0.9"/>
            <stop offset="100%" stop-color="var(--ray-glow)" stop-opacity="0"/>
          </radialGradient>
        </defs>
        <g role="img" aria-label="Sunburst of fine golden rays radiating behind the brand name">
          <circle cx="180" cy="300" r="250" fill="url(#sunburstGlow)"/>
        </g>
        <g role="img" aria-label="Large golden sun emblem behind the brand name">
          <circle cx="180" cy="300" r="95" fill="var(--sun-yellow)" opacity="0.85"/>
        </g>
        <path class="band-cream" d="M0 430 C 90 400, 200 460, 360 410 L 360 680 L 0 680 Z" fill="var(--cream-band)"/>
        <path class="band-peach" d="M0 500 C 100 470, 220 520, 360 480 L 360 680 L 0 680 Z" fill="var(--peach-band)"/>
        <path class="band-mango" d="M0 620 C 60 600, 90 560, 150 590 C 220 625, 280 560, 360 570 L 360 680 L 0 680 Z" fill="var(--mango-yellow)"/>
      </svg>
      <p class="calorie-count">100 CALORIES</p>
      <h1 class="brand-name">VELKA</h1>
      <h2 class="flavor-name">MANGO-ORANGE</h2>
      <p class="beverage-type">VODKA SPIKED SELTZER</p>
      <p class="product-facts"><span>NO SUGAR</span><span>5% ALCOHOL</span></p>
    </section>
  </main>
</body>
</html>
```